Management Consulting needing a cool business card for client acquisition and networking

We are looking for a business card that is progressive and fresh that conveys innovation, forward thinking, and confidence. The business card is for a company based in Charlotte NC called, 'MERIDOX CONSULTING GROUP LLC'. The company primarily works with banks, insurance, and brokerages to implement innovative solutions to help them streamline their operations, to more effectively manage risks, and to improve their customer relationships.

Target Market(s)

Typically meet with Chief Financial Officers, Chief Information Officers, Chief Operations Officer, Business Unit Leader. The target market are generally 40-55 years, male, white, master level education plus.

Industry/Entity Type

Progressive

Font styles to use
Serif
Other font styles liked:
• Calibri

Requirements
Should not have
• Designs that look too much like law firms or accounting companies. Too conservative

```html
<!DOCTYPE html>
<html lang="en">
<head>
<meta charset="utf-8">
<title>Meridox Consulting Group – Business Card</title>
<link rel="stylesheet" href="https://fonts.googleapis.com/css2?family=Carlito:wght@400;700&display=swap">
<style>
  :root {
    --page: #ffffff;
    --card-blue: #1b8cb6;
    --pill-blue: #3ab6e2;
    --bright-blue: #19c2f0;
    --stripe-dark: #17242c;
    --panel: #ecebe6;
    --ink: #16232b;
  }
  * { margin: 0; padding: 0; box-sizing: border-box; }
  html, body { width: 1200px; height: 434px; overflow: hidden; background: var(--page); }
  body { position: relative; font-family: "Carlito", "Calibri", sans-serif; color: var(--ink); }

  .card {
    position: absolute;
    top: 97px;
    width: 356px;
    height: 205px;
    background: var(--card-blue);
    overflow: hidden;
  }
  .card--front { left: 200px; }
  .card--back { left: 650px; }

  .brand {
    position: absolute;
    display: flex; align-items: center; gap: 5px;
    font-weight: 700; color: var(--ink); white-space: nowrap;
  }
  .brand__square { display: block; background: var(--ink); }

  /* front */
  .brand--front { left: 8px; top: 19px; font-size: 13px; letter-spacing: .5px; }
  .brand--front .brand__square { width: 8px; height: 8px; }
  .company-pill {
    position: absolute; left: 86px; top: 11px; width: 268px; height: 24px;
    border-radius: 12px; background: var(--pill-blue);
    font-size: 15px; color: var(--ink); letter-spacing: .3px;
    display: flex; align-items: center; justify-content: center; white-space: nowrap;
  }
  .front-band { position: absolute; left: 0; top: 57px; width: 100%; height: 7px; background: var(--stripe-dark); }
  .swirl-corner { position: absolute; left: 0; top: 172px; width: 30px; height: 33px;
    background: radial-gradient(circle at 0 100%, var(--stripe-dark), #2b4f60 70%, transparent 72%); }
  .info-panel {
    position: absolute; left: 7px; top: 77px; width: 346px; height: 122px;
    background: var(--panel); border-radius: 14px;
  }
  .panel-dot {
    position: absolute; left: 316px; top: 90px; width: 32px; height: 32px;
    border-radius: 50%; background: var(--card-blue);
  }
  .person { position: absolute; left: 0; top: 98px; width: 356px; text-align: center; }
  .person__name { font-size: 12px; letter-spacing: .4px; line-height: 14px; }
  .person__title { font-size: 8.5px; font-weight: 700; line-height: 12px; }
  .address {
    position: absolute; right: 196px; top: 140px; text-align: right;
    font-size: 9px; line-height: 20px; white-space: nowrap;
  }
  .contact {
    position: absolute; left: 193px; top: 140px;
    font-size: 9px; line-height: 13px; white-space: nowrap;
  }

  /* back */
  .ornament {
    position: absolute; left: 220px; top: 18px; width: 136px; height: 115px;
    background: radial-gradient(ellipse at 70% 45%, rgba(25,194,240,.55), rgba(25,194,240,0) 70%);
  }
  .back-line { position: absolute; left: 0; top: 134px; width: 100%; height: 2px; background: var(--bright-blue); }
  .back-stripe { position: absolute; left: 0; top: 141px; width: 100%; height: 14px; background: var(--stripe-dark); }
  .rings-left { position: absolute; left: 0; top: 152px; width: 72px; height: 53px;
    background: radial-gradient(circle at 40% 100%, var(--stripe-dark), #203744 65%, transparent 67%); }
  .rings-right { position: absolute; left: 250px; top: 140px; width: 106px; height: 65px;
    background: radial-gradient(circle at 75% 95%, var(--bright-blue), rgba(25,194,240,.4) 55%, transparent 70%); }
  .brand--back { left: 108px; top: 90px; font-size: 19px; letter-spacing: .8px; }
  .brand--back .brand__square { width: 11px; height: 11px; }
</style>
</head>
<body>
  <section class="card card--front">
    <div class="brand brand--front"><span class="brand__square"></span><span>MERIDOX</span></div>
    <div class="company-pill">MERIDOX CONSULTING GROUP LLC</div>
    <div class="front-band"></div>
    <div class="swirl-corner" role="img" aria-label="Dark concentric ring decoration"></div>
    <div class="info-panel"></div>
    <div class="panel-dot"></div>
    <div class="person">
      <p class="person__name">JONAS R. VALE</p>
      <p class="person__title">CHIEF SOLUTION ARCHITECT</p>
    </div>
    <div class="address">
      <p>2715 LAKEMONT DR, SUITE 210</p>
      <p>Charlotte, NC 28209</p>
    </div>
    <div class="contact">
      <p>o: 704.555.0142</p>
      <p>c: 704.555.0187</p>
      <p>e: jvale@meridoxconsulting.com</p>
    </div>
  </section>

  <section class="card card--back">
    <div class="ornament" role="img" aria-label="Light blue floral swirl ornament"></div>
    <div class="back-line"></div>
    <div class="back-stripe"></div>
    <div class="rings-left" role="img" aria-label="Dark concentric ring decoration"></div>
    <div class="rings-right" role="img" aria-label="Bright blue concentric ring decoration"></div>
    <div class="brand brand--back"><span class="brand__square"></span><span>MERIDOX</span></div>
  </section>
</body>
</html>
```